Stylish new business card needed!

Hello everyone! I am in need of a new business card design for an alarm company here in Hurricane WV. I have all fonts, color codes and logos provided for you use! We are a young company and like the style of a clean sleek looking business card. Would like it double sided, one side holding the logo and the other with your design!
Target Market(s)
The people that are looking for the newest tech for home automation and security
Industry/Entity Type
Alarm services; Home automation
Contact Information for Business Card
Name of person; position (Sales; Installer); Phone Number (555.419.7362); Employee cell Number; Website (www.GuardedByVelm.example); Employee Email; Double sided
Look and feel
Each slider illustrates characteristics of the customer's brand and the style your logo design should communicate.

```html
<!DOCTYPE html>
<html lang="en">
<head>
<meta charset="utf-8">
<title>Velm Business Card</title>
<link rel="stylesheet" href="https://fonts.googleapis.com/css2?family=Archivo+Black&family=Arimo:wght@400;700&display=swap">
<style>
  :root {
    --stage: #3b3b3b;
    --paper: #ffffff;
    --brand-orange: #f39150;
    --brand-grey: #999999;
    --ink: #1c1c1c;
  }
  * { box-sizing: border-box; margin: 0; padding: 0; }
  html, body { width: 1200px; height: 689px; overflow: hidden; }
  body {
    background: var(--stage);
    display: flex;
    align-items: center;
    justify-content: center;
    gap: 36px;
    font-family: "Arimo", Arial, sans-serif;
  }
  .card {
    position: relative;
    width: 546px;
    height: 312px;
    background: var(--paper);
    overflow: hidden;
  }
  .wordmark {
    display: flex;
    align-items: center;
    gap: 14px;
  }
  .wordmark-dot {
    border-radius: 50%;
    background: var(--brand-orange);
  }
  .wordmark-name {
    font-family: "Arimo", Arial, sans-serif;
    font-weight: 400;
    color: var(--brand-grey);
    letter-spacing: 2px;
    line-height: 1;
  }

  /* Front side */
  .card-front {
    display: flex;
    flex-direction: column;
    align-items: center;
    justify-content: center;
    gap: 14px;
  }
  .card-front .wordmark-dot { width: 46px; height: 46px; }
  .card-front .wordmark-name { font-size: 96px; }
  .tagline {
    font-family: "Archivo Black", "Arial Black", sans-serif;
    color: var(--brand-orange);
    font-size: 13px;
    letter-spacing: 1.2px;
    text-transform: uppercase;
  }

  /* Back side */
  .swoosh { position: absolute; inset: 0; }
  .card-back .wordmark {
    position: absolute;
    top: 34px;
    right: 60px;
  }
  .card-back .wordmark-dot { width: 26px; height: 26px; }
  .card-back .wordmark-name { font-size: 62px; }
  .person {
    position: absolute;
    left: 40px;
    top: 96px;
  }
  .person-name {
    font-family: "Archivo Black", "Arial Black", sans-serif;
    font-size: 24px;
    letter-spacing: 0.5px;
    text-transform: uppercase;
    color: var(--brand-grey);
  }
  .person-name .surname { color: var(--brand-orange); }
  .person-role { font-size: 16px; color: var(--ink); margin-top: 2px; }
  .contacts {
    position: absolute;
    left: 40px;
    top: 158px;
    list-style: none;
  }
  .contacts li {
    display: flex;
    align-items: center;
    gap: 10px;
    font-size: 15px;
    color: var(--ink);
    line-height: 22px;
  }
  .contacts svg { width: 13px; height: 13px; fill: var(--brand-orange); flex: none; }
</style>
</head>
<body>

  <section class="card card-front" aria-label="Card front">
    <div class="wordmark">
      <span class="wordmark-dot"></span>
      <span class="wordmark-name">VELM</span>
    </div>
    <p class="tagline">Automation and Security Services</p>
  </section>

  <section class="card card-back" aria-label="Card back">
    <svg class="swoosh" viewBox="0 0 546 312" preserveAspectRatio="none" aria-hidden="true">
      <path d="M0 312 L546 312 L546 56 C492 232 300 304 0 304 Z" fill="var(--brand-orange)"/>
      <path d="M0 298 C300 298 486 226 540 48" fill="none" stroke="var(--paper)" stroke-width="8"/>
      <path d="M0 294 C300 294 482 222 534 42" fill="none" stroke="var(--brand-grey)" stroke-width="4"/>
    </svg>

    <div class="wordmark">
      <span class="wordmark-dot"></span>
      <span class="wordmark-name">VELM</span>
    </div>

    <div class="person">
      <p class="person-name">Evan <span class="surname">Mercer</span></p>
      <p class="person-role">Sales; Installer</p>
    </div>

    <ul class="contacts">
      <li>
        <svg viewBox="0 0 16 16" aria-hidden="true"><path d="M3 1l3 3-2 2c1 2 3 4 5 5l2-2 3 3-2 3C6 15 1 10 1 3z"/></svg>
        555.419.7362
      </li>
      <li>
        <svg viewBox="0 0 16 16" aria-hidden="true"><path d="M4 0h8a1 1 0 0 1 1 1v14a1 1 0 0 1-1 1H4a1 1 0 0 1-1-1V1a1 1 0 0 1 1-1zm1 2v10h6V2zm3 11a1 1 0 1 0 0 2 1 1 0 0 0 0-2z"/></svg>
        555.419.7380
      </li>
      <li>
        <svg viewBox="0 0 16 16" aria-hidden="true"><path d="M0 3h16v1L8 9 0 4zm0 3l8 5 8-5v7H0z"/></svg>
        info@GuardedByVelm.example
      </li>
      <li>
        <svg viewBox="0 0 16 16" aria-hidden="true"><circle cx="8" cy="8" r="7.5"/></svg>
        www.GuardedByVelm.example
      </li>
    </ul>
  </section>

</body>
</html>
```